ORK Brantell Services - Partnership Proposal

My company ORK is a study abroad consultant and We want to send a proposal to Universities and Educational institutions to partner with us. This proposal shall be used by our marketing team to collaborate with more than 100 top universities of the world and hence it must look like an extremely professional presentation.

Target Market(s)

Education institutions and Universities

Industry/Entity Type

Education

Font styles to use
Serif

Colors

Designer to choose colors to be used in the design.

Requirements
Must have
• A professional and neat look with company logo.
Nice to have
• Would like to see some the text presented in an interesting eye catchy manner.
Should not have
• Should not have too many colours or different fonts

```html
<!DOCTYPE html>
<html lang="en">
<head>
<meta charset="utf-8">
<title>ORK Brantell Services – Partnership Proposal</title>
<link rel="stylesheet" href="https://fonts.googleapis.com/css2?family=Open+Sans:ital,wght@0,400;0,600;0,700;0,800;1,600;1,700&family=Oswald:wght@500&display=swap">
<style>
  :root {
    --ink: #2b2b2d;
    --dark-band: #333335;
    --orange: #f7a81b;
    --white: #ffffff;
    --body-text: #333333;
    --backdrop: #1f1f20;
  }
  * { margin: 0; padding: 0; box-sizing: border-box; }
  html, body { width: 945px; height: 1200px; overflow: hidden; }
  body { background: var(--backdrop); font-family: "Open Sans", Arial, sans-serif; position: relative; }

  .flyer { position: absolute; left: 80px; top: 92px; width: 785px; height: 1015px; background: var(--white); overflow: hidden; }

  .brand { position: absolute; left: 80px; top: 22px; }
  .brand-name { font-size: 74px; font-weight: 800; line-height: 1; color: var(--ink); letter-spacing: 2px; }
  .brand-tagline { margin-top: 4px; font-size: 12.5px; font-weight: 700; color: var(--orange); letter-spacing: .3px; }

  .services { position: absolute; right: 92px; top: 58px; font-family: "Oswald", sans-serif; font-weight: 500; font-size: 22px; color: var(--ink); display: flex; gap: 8px; }
  .services span::before { content: "|"; color: var(--orange); margin-right: 8px; }

  .header-rule { position: absolute; left: 0; top: 118px; width: 100%; height: 7px; background: var(--ink); }

  .hero-photo { position: absolute; left: 0; top: 125px; width: 100%; height: 551px;
    background: linear-gradient(100deg, #e9c66a 0%, #d9d2c2 30%, #c9ccd1 55%, #9aa3ad 80%, #6f7a86 100%); }

  .title-band { position: absolute; left: 0; top: 246px; width: 410px; height: 160px; background: rgba(255,255,255,.86); }
  .title { position: absolute; left: 40px; top: 266px; font-size: 36px; font-weight: 800; line-height: 44px; color: var(--ink); }
  .title em { font-style: normal; color: var(--orange); }

  .caption-box { position: absolute; left: 391px; top: 585px; width: 394px; height: 91px; background: rgba(43,43,45,.88);
    font-family: "Oswald", sans-serif; font-weight: 500; font-size: 21px; color: var(--white); text-align: center; line-height: 91px; }
  .caption-strip { position: absolute; left: 391px; top: 676px; width: 394px; height: 14px; background: var(--orange); }

  .about-panel { position: absolute; left: 0; top: 441px; width: 391px; height: 450px; background: var(--white); border-top-right-radius: 32px; }

  .section-tag { position: absolute; height: 23px; background: var(--orange); color: var(--ink); font-size: 13.5px; font-weight: 700;
    line-height: 23px; padding-left: 11px; clip-path: polygon(0 0, 91% 0, 100% 100%, 0 100%); }
  .about-tag { left: 46px; top: 470px; width: 250px; }
  .partner-tag { left: 393px; top: 710px; width: 250px; }

  .about-text { position: absolute; left: 46px; top: 507px; width: 318px; font-size: 11.4px; line-height: 16.4px; color: var(--body-text); }
  .about-text p + p { margin-top: 16px; }

  .reasons { position: absolute; left: 393px; top: 748px; list-style: none; }
  .reasons li { display: flex; align-items: center; gap: 10px; height: 36px; margin-bottom: 11px; font-size: 13.6px; font-weight: 700; line-height: 17px; color: var(--ink); }
  .reasons svg { flex: none; }

  .footer { position: absolute; left: 0; top: 891px; width: 100%; height: 116px; background: var(--dark-band); }
  .footer-rule { position: absolute; left: 0; top: 1007px; width: 100%; height: 8px; background: var(--orange); }
  .contact { position: absolute; left: 49px; top: 908px; }
  .contact-lead { font-size: 13.8px; font-weight: 700; line-height: 18px; color: var(--orange); }
  .contact-phone { margin-top: 8px; font-size: 21px; font-weight: 700; color: var(--orange); }
  .contact-web { margin-top: 4px; font-size: 13.5px; font-weight: 700; color: var(--white); }

  .channels { position: absolute; left: 318px; top: 911px; list-style: none; font-size: 11.6px; line-height: 17.6px; color: var(--white); font-style: italic; }
  .channels li::before { content: ""; display: inline-block; width: 5px; height: 5px; background: var(--orange); margin-right: 8px; vertical-align: middle; }
  .channels b { color: var(--orange); font-weight: 700; }
  .channels-note { position: absolute; left: 318px; top: 964px; width: 430px; font-size: 11.6px; line-height: 15px; font-weight: 700; font-style: italic; color: var(--white); }
</style>
</head>
<body>
  <main class="flyer">
    <div class="brand">
      <div class="brand-name">ORK</div>
      <div class="brand-tagline">GLOBAL EDUCATION ADVICE</div>
    </div>
    <nav class="services"><span>STUDY</span><span>WORK</span><span>BUSINESS</span><span>TOURS</span></nav>
    <div class="header-rule"></div>

    <div class="hero-photo" role="img" aria-label="Photo of a traveller walking with a suitcase through a bright airport terminal"></div>
    <div class="title-band"></div>
    <h1 class="title">PROPOSAL<br>TO <em>REPRESENT</em><br>YOUR INSTITUTION</h1>
    <div class="caption-box">NEW ZEALAND’S BEST MIGRATION ADVISOR</div>
    <div class="caption-strip"></div>

    <div class="about-panel"></div>
    <h2 class="section-tag about-tag">ABOUT US</h2>
    <div class="about-text">
      <p>ORK Brantell Services Limited is a New Zealand based company established in 2013, engaged in providing end-to-end study abroad and migration services to international students and families. Headed by a Licensed Immigration Adviser with a strong social media presence and a sales &amp; service team operating from different parts of the world. ORK has been servicing clients from more than 30 countries of the world like India, Sri Lanka, Maldives, UAE, Egypt, Brazil, etc. The company boasts of being a specialist in New Zealand student enrollment and also offers after arrival support by an experienced and efficient onshore team.</p>
      <p>ORK is proud to have successfully served all the leading New Zealand Institutions. Having spent over a decade in this pursuit and realizing the ever increasing growth of study abroad aspirants, the core team of ORK is now keen to expand into other countries and set a global footprint in overseas education domain. Our consistent and creative social media marketing initiatives are attracting topnotch students from different countries to study in high quality global institutions.</p>
    </div>

    <h2 class="section-tag partner-tag">WHY PARTNER WITH US?</h2>
    <ul class="reasons">
      <li><svg width="34" height="34" viewBox="0 0 34 34"><rect x="2" y="2" width="30" height="30" rx="6" fill="none" stroke="#2b2b2d" stroke-width="3"/><path d="M9 17l6 6 11-12" fill="none" stroke="#f7a81b" stroke-width="4" stroke-linecap="round" stroke-linejoin="round"/></svg><span>PROVEN TRACK RECORD OF STUDENT<br>ENROLLMENT FOR NEW ZEALAND</span></li>
      <li><svg width="34" height="34" viewBox="0 0 34 34"><rect x="2" y="2" width="30" height="30" rx="6" fill="none" stroke="#2b2b2d" stroke-width="3"/><path d="M9 17l6 6 11-12" fill="none" stroke="#f7a81b" stroke-width="4" stroke-linecap="round" stroke-linejoin="round"/></svg><span>HIGH CONVERSION RATE -<br>APPLICATION TO ENROLMENT</span></li>
      <li><svg width="34" height="34" viewBox="0 0 34 34"><rect x="2" y="2" width="30" height="30" rx="6" fill="none" stroke="#2b2b2d" stroke-width="3"/><path d="M9 17l6 6 11-12" fill="none" stroke="#f7a81b" stroke-width="4" stroke-linecap="round" stroke-linejoin="round"/></svg><span>QUALIFIED AND EXPERIENCED TEAM<br>ACROSS COUNTRIES</span></li>
    </ul>

    <footer class="footer"></footer>
    <div class="contact">
      <div class="contact-lead">FOR MORE INFORMATION<br>CALL OR VISIT TODAY</div>
      <div class="contact-phone">Call &nbsp;: 000 000 0000</div>
      <div class="contact-web">WWW.ORKBRANTELL.COM</div>
    </div>
    <ul class="channels">
      <li><b>Friendbook Page:</b> https://www.friendbook.example/orkstudyadviser/</li>
      <li><b>Friendbook Group:</b> https://www.friendbook.example/groups/ORKOptions/</li>
      <li><b>ViewTube Channel :</b> https://www.viewtube.example/channel/ORKstudyabroad2013NZ</li>
    </ul>
    <p class="channels-note">We will utilise all these social media platforms proactively to promote the courses being offered by your institution.</p>
    <div class="footer-rule"></div>
  </main>
</body>
</html>
```